Brevanta needs a business Card Design

We are looking for a business card Design for our new Managed Service Provider Company, Brevanta. Brevanta encompasses everything IT for the average medium sized business. Our primary services are help desk support, cyber-security (malware and ransomware protection), and Disaster Recovery systems. We would like the design to have a very clean and professional look, with a very minimalist feel.

Target Market(s)

Medium to large sized businesses

Industry/Entity Type

It Service

Contact Information for Business Card

Name GoesHere
name@brevanta-mail.net
O: 555-382-6047
C: 555-000-0000

Font styles to use
Other font styles liked:
• Poppins Font Only Please

Colors

Designer to choose only greyscale colors for use in the design.

Requirements
Must have
• Logo included
Nice to have
• Cutting Edge, innovative, minimalistic, elegant

```html
<!DOCTYPE html>
<html lang="en">
<head>
<meta charset="utf-8">
<title>Brevanta Business Card</title>
<link href="https://fonts.googleapis.com/css2?family=Poppins:wght@300;400;500;600&display=swap" rel="stylesheet">
<style>
  :root {
    --backdrop: #a8a8a8;
    --charcoal: #222222;
    --paper: #ffffff;
    --ink: #1e1e1e;
    --muted: #6e6e6e;
    --rule: #3a3a3a;
  }
  * { margin: 0; padding: 0; box-sizing: border-box; }
  html, body { width: 1200px; height: 930px; overflow: hidden; }
  body {
    background: var(--backdrop);
    font-family: "Poppins", sans-serif;
    position: relative;
  }
  .card {
    position: absolute;
    width: 525px;
    height: 300px;
    border-radius: 18px;
    top: 315px;
    box-shadow: 0 6px 16px rgba(0,0,0,0.18);
  }
  .card-back { left: 50px; background: var(--charcoal); }
  .card-front { left: 625px; background: var(--paper); color: var(--ink); }

  .back-wordmark {
    position: absolute;
    top: 50%; left: 50%;
    transform: translate(-50%, -50%);
    color: var(--paper);
    font-weight: 400;
    font-size: 26px;
    letter-spacing: 8px;
    text-transform: uppercase;
    white-space: nowrap;
  }

  .front-wordmark {
    position: absolute;
    top: 44px; right: 34px;
    display: flex; align-items: center; gap: 10px;
    font-weight: 400;
    font-size: 19px;
    letter-spacing: 7px;
    text-transform: uppercase;
    color: var(--ink);
    white-space: nowrap;
  }
  .front-wordmark .mark {
    width: 12px; height: 12px; background: var(--ink);
  }
  .divider {
    position: absolute;
    left: 30px; right: 30px; top: 112px;
    height: 1px; background: var(--rule);
  }
  .person { position: absolute; left: 30px; top: 130px; }
  .person-name { font-weight: 600; font-size: 19px; letter-spacing: 0.5px; text-transform: uppercase; color: var(--ink); }
  .person-title { font-weight: 400; font-size: 12px; color: var(--muted); margin-top: 1px; }
  .person-rule { width: 90px; height: 1px; background: var(--rule); margin: 10px 0 8px; }
  .contacts { list-style: none; font-weight: 300; font-size: 12.5px; color: var(--muted); }
  .contacts li { display: flex; align-items: center; gap: 7px; line-height: 19px; white-space: nowrap; }
  .contacts svg { width: 10px; height: 10px; flex: none; color: var(--ink); }
  .address {
    position: absolute; right: 30px; top: 132px;
    text-align: right; font-weight: 300; font-size: 12.5px; line-height: 19px; color: var(--muted);
  }
</style>
</head>
<body>
  <section class="card card-back">
    <div class="back-wordmark">Brevanta</div>
  </section>

  <section class="card card-front">
    <div class="front-wordmark"><span class="mark"></span>Brevanta</div>
    <div class="divider"></div>

    <div class="person">
      <div class="person-name">Daniel Reyes</div>
      <div class="person-title">Director</div>
      <div class="person-rule"></div>
      <ul class="contacts">
        <li><svg viewBox="0 0 10 10"><path d="M2 1l2 2-1 1.2a6 6 0 0 0 2.8 2.8L7 6l2 2-1.2 1.2C4.5 9 1 5.5 0.8 2.2z" fill="currentColor"/></svg>555-382-6047</li>
        <li><svg viewBox="0 0 10 10"><rect x="2.5" y="0.5" width="5" height="9" rx="1" fill="none" stroke="currentColor"/><circle cx="5" cy="7.8" r="0.6" fill="currentColor"/></svg>555-000-0000</li>
        <li><svg viewBox="0 0 10 10"><rect x="0.5" y="2" width="9" height="6" fill="none" stroke="currentColor"/><path d="M0.5 2l4.5 3.5L9.5 2" fill="none" stroke="currentColor"/></svg>daniel@brevanta-mail.net</li>
        <li><svg viewBox="0 0 10 10"><circle cx="5" cy="5" r="4.3" fill="none" stroke="currentColor"/><path d="M0.7 5h8.6M5 0.7c-2.4 2.6-2.4 6 0 8.6M5 0.7c2.4 2.6 2.4 6 0 8.6" fill="none" stroke="currentColor" stroke-width="0.8"/></svg>www.danielbrevanta.net</li>
      </ul>
    </div>

    <div class="address">48 Harlow Avenue<br>Fairview, TN 37062</div>
  </section>
</body>
</html>
```